弊社のサービスが一目で伝わるデザインを希望します。コロナ禍でチラシを受け取りたくない方も大勢いらっしゃると思いますが、そんな中でも手に取っていただけるような明るい雰囲気が良いかと思います。サービスの良い点を前面にアピールしてください。両面希望ですが、ポスターにも流用希望ですので、片面でも充分伝わる内容でお願いします。弊社サービスは3パターンあり、パンフレットに挟んでお客様へお渡ししたいと思います。3パターン合計の費用となります。

```html
<!DOCTYPE html>
<html lang="ja">
<head>
<meta charset="utf-8">
<title>健康診断BPOサービス</title>
<link href="https://fonts.googleapis.com/css2?family=Noto+Sans+JP:wght@400;500;700;900&display=swap" rel="stylesheet">
<style>
  :root {
    --navy: #15306e;
    --blue: #1f63c4;
    --sky: #3d8fe0;
    --pale: #e9f3fc;
    --orange: #f07a12;
    --yellow: #ffe83a;
    --red: #d9312a;
    --ink: #1a1a1a;
    --white: #ffffff;
  }
  * { box-sizing: border-box; margin: 0; padding: 0; }
  html, body { width: 847px; height: 1200px; overflow: hidden; }
  body { font-family: "Noto Sans JP", sans-serif; color: var(--ink); background: var(--white); }
  .flyer {
    position: relative; width: 847px; height: 1200px; overflow: hidden;
    background: linear-gradient(180deg, #ffffff 0%, #ffffff 45%, var(--pale) 60%, #dcebf9 100%);
  }
  .hero-photo {
    position: absolute; left: 494px; top: 0; width: 353px; height: 600px;
    background: linear-gradient(160deg, #f6f9fc 0%, #e4edf6 55%, #cfdff0 100%);
  }
  .service-label {
    position: absolute; left: 28px; top: 22px;
    font-size: 22px; font-weight: 700; color: var(--navy); letter-spacing: 1px;
  }
  .service-label span { color: var(--blue); margin-left: 10px; }
  .side-note {
    position: absolute; right: 20px; top: 28px;
    writing-mode: vertical-rl; font-size: 17px; font-weight: 700; color: var(--red);
  }
  .audience {
    position: absolute; left: 34px; top: 80px; padding: 2px 18px;
    background: var(--blue); color: var(--white); font-size: 34px; font-weight: 900;
    transform: skewX(-8deg); letter-spacing: 1px;
  }
  .audience span { display: inline-block; transform: skewX(8deg); }
  .headline {
    position: absolute; left: 36px; top: 124px;
    font-size: 64px; font-weight: 900; line-height: 76px; letter-spacing: 1px; color: var(--ink);
    text-shadow: 0 0 6px #fff, 0 0 6px #fff;
  }
  .solve { position: absolute; left: 90px; top: 270px; width: 500px; height: 170px; }
  .band {
    position: absolute; left: 34px; top: 432px; width: 779px; height: 146px;
    background: linear-gradient(90deg, var(--blue), var(--sky));
    text-align: center; color: var(--white); padding-top: 12px;
  }
  .band-lead { font-size: 38px; font-weight: 900; letter-spacing: 1px; }
  .band-title { font-size: 52px; font-weight: 900; color: var(--yellow); letter-spacing: 2px; line-height: 68px; }
  .question {
    position: absolute; left: 0; width: 847px; top: 590px; text-align: center;
    font-size: 32px; font-weight: 900; color: var(--navy);
  }
  .worries { position: absolute; left: 34px; top: 638px; width: 779px; display: flex; gap: 11px; }
  .worry {
    flex: 1; height: 208px; background: var(--white); border: 2px solid var(--navy);
    padding: 10px 10px 0; display: flex; flex-direction: column;
  }
  .worry-text { font-size: 20px; font-weight: 700; line-height: 28px; color: var(--navy); }
  .worry-text em { font-style: normal; color: var(--red); }
  .worry-art {
    margin-top: auto; height: 78px; margin-bottom: 8px;
    background: linear-gradient(180deg, #eef4fb, #d5e5f5); border-radius: 4px;
  }
  .resolve {
    position: absolute; left: 0; width: 847px; top: 852px; text-align: center;
    font-size: 33px; font-weight: 900; color: var(--orange);
  }
  .merits {
    position: absolute; left: 34px; top: 904px; width: 779px; height: 196px;
    border: 2px solid var(--blue); background: var(--white);
  }
  .merits-title {
    position: absolute; left: 50%; top: -2px; transform: translateX(-50%);
    background: var(--blue); color: var(--white); font-size: 20px; font-weight: 700;
    padding: 2px 40px;
  }
  .merit-list { display: flex; height: 100%; padding: 36px 14px 12px; gap: 12px; }
  .merit { flex: 1; display: flex; flex-direction: column; border-right: 1px dashed #9bb9e0; padding-right: 12px; }
  .merit:last-child { border-right: none; padding-right: 0; }
  .merit p { font-size: 14px; line-height: 20px; color: var(--navy); }
  .merit-icon { margin-top: auto; align-self: center; }
  .company {
    position: absolute; left: 34px; top: 1120px; width: 680px; text-align: center;
    font-size: 32px; font-weight: 900; color: var(--navy); letter-spacing: 1px;
  }
  .back-note {
    position: absolute; right: 30px; top: 1118px; width: 110px;
    border: 1px solid var(--navy); padding: 4px 6px;
    font-size: 11px; line-height: 16px; color: var(--navy); background: var(--white);
  }
</style>
</head>
<body>
<div class="flyer">
  <div class="hero-photo" role="img" aria-label="笑顔で案内する医療スタッフの写真"></div>

  <div class="service-label">健康診断<span>予約コールセンターサービス</span></div>
  <div class="side-note">面倒な業務が改善!</div>

  <div class="audience"><span>医療機関様、企業様へ</span></div>
  <div class="headline">面倒な医療機関の<br>窓口業務の問題を</div>

  <svg class="solve" viewBox="0 0 500 170" aria-label="解決">
    <text x="10" y="150" font-family="Noto Sans JP, sans-serif" font-weight="900" font-size="160"
      letter-spacing="50" fill="#f07a12" stroke="#ffffff" stroke-width="10" paint-order="stroke">解決</text>
  </svg>

  <div class="band">
    <div class="band-lead">医療機関の窓口業務をスムーズにする</div>
    <div class="band-title">健康診断BPOサービス</div>
  </div>

  <div class="question">こんな事でお悩みではありませんか?</div>

  <div class="worries">
    <div class="worry">
      <div class="worry-text">各事業所の<br>健診予約を<em>とり<br>まとめる</em>のが大変</div>
      <div class="worry-art" role="img" aria-label="書類を抱える担当者のイラスト"></div>
    </div>
    <div class="worry">
      <div class="worry-text">残業している<br>スタッフの<br><em>業務を軽減</em><br>させたい</div>
      <div class="worry-art" role="img" aria-label="残業するスタッフのイラスト"></div>
    </div>
    <div class="worry">
      <div class="worry-text">他の業務が<br>忙しく、<em>受付電<br>話に出る余裕</em><br>がない</div>
      <div class="worry-art" role="img" aria-label="鳴り続ける電話のイラスト"></div>
    </div>
    <div class="worry">
      <div class="worry-text">閑散期の<br>スタッフの<br><em>人件費</em>を<br>見直したい</div>
      <div class="worry-art" role="img" aria-label="人件費を考えるスタッフのイラスト"></div>
    </div>
  </div>

  <div class="resolve">このような問題を健康診断BPOサービスで解決!</div>

  <div class="merits">
    <div class="merits-title">導入のメリット</div>
    <div class="merit-list">
      <div class="merit">
        <p>予約受付数に比例し費用が変動するため、繁閑の差があっても無駄なコストを抑えられます。</p>
        <svg class="merit-icon" width="56" height="56" viewBox="0 0 56 56"><circle cx="28" cy="28" r="24" fill="none" stroke="#1f63c4" stroke-width="3"/><text x="28" y="37" text-anchor="middle" font-size="24" font-weight="700" fill="#1f63c4" font-family="Noto Sans JP, sans-serif">¥</text></svg>
      </div>
      <div class="merit">
        <p>予約受付業務をアウトソースすることで、スタッフが本来の業務に集中できます。</p>
        <svg class="merit-icon" width="56" height="56" viewBox="0 0 56 56"><rect x="8" y="12" width="40" height="30" rx="3" fill="none" stroke="#1f63c4" stroke-width="3"/><path d="M20 27l6 6 11-12" fill="none" stroke="#f07a12" stroke-width="3"/></svg>
      </div>
      <div class="merit">
        <p>経験豊富なオペレーターが丁寧に対応し、受診者の満足度向上につながります。</p>
        <svg class="merit-icon" width="56" height="56" viewBox="0 0 56 56"><path d="M16 10c-4 0-6 4-6 8 0 14 14 28 28 28 4 0 8-2 8-6l-8-6-5 4c-5-2-9-6-11-11l4-5z" fill="none" stroke="#1f63c4" stroke-width="3"/></svg>
      </div>
      <div class="merit">
        <p>お客様のご希望に合わせて柔軟に対応し、予約状況の共有もスムーズに行えます。</p>
        <svg class="merit-icon" width="56" height="56" viewBox="0 0 56 56"><circle cx="20" cy="22" r="8" fill="none" stroke="#1f63c4" stroke-width="3"/><circle cx="38" cy="22" r="8" fill="none" stroke="#1f63c4" stroke-width="3"/><path d="M6 46c2-8 8-12 14-12s12 4 14 12M24 46c2-8 8-12 14-12s10 4 12 12" fill="none" stroke="#1f63c4" stroke-width="3"/></svg>
      </div>
    </div>
  </div>

  <div class="company">株式会社ミライサポートサイエンス</div>
  <div class="back-note">詳細、お問い合わせは裏面をご覧ください</div>
</div>
</body>
</html>
```